Bed & Breakfast Business Card Design

Casa Verbena Bed & Breakfast is a private, adult-only, upscale retreat for guests vacationing or on business in the Atlanta area.

Event venue for weddings & retreats

Target Market(s)

Age 40+ couples, romantic get-aways, honeymoon, small weddings, business retreats

Industry/Entity Type

Business

Contact Information for Business Card

Casa Verbena Bed & Breakfast, LLC
3187 Partridge Fen Road
Palmetto, GA 30268
770-555-0193
www.CasaVerbenaRetreat.example

```html
<!DOCTYPE html>
<html lang="en">
<head>
<meta charset="utf-8">
<title>Casa Verbena Bed &amp; Breakfast – Business Card</title>
<link rel="stylesheet" href="https://fonts.googleapis.com/css2?family=Arimo:wght@400&display=swap">
<style>
  :root {
    --stage: #5e5e5e;
    --card-gold: #bfa572;
    --ink: #4a4a4a;
    --tagline: #f4efe6;
    --accent-peach: #e6c3a0;
    --card-white: #ffffff;
    --back-edge: #5e5e5e;
    --back-border: #111111;
    --back-ink: #444444;
  }
  * { box-sizing: border-box; margin: 0; padding: 0; }
  html, body {
    width: 1200px;
    height: 900px;
    overflow: hidden;
    background: var(--stage);
    font-family: "Arimo", Arial, sans-serif;
  }
  .canvas {
    position: relative;
    width: 1200px;
    height: 900px;
  }
  .card-front {
    position: absolute;
    left: 48px;
    top: 291px;
    width: 521px;
    height: 305px;
    background: var(--card-gold);
  }
  .brand {
    position: absolute;
    left: 0;
    right: 0;
    top: 80px;
    display: flex;
    flex-direction: column;
    align-items: center;
    color: var(--ink);
  }
  .brand-mark {
    width: 56px;
    height: 56px;
    background: var(--accent-peach);
    margin-bottom: 22px;
  }
  .brand-name {
    font-size: 36px;
    line-height: 1;
    letter-spacing: 0.5px;
  }
  .brand-rule {
    width: 224px;
    height: 2px;
    background: var(--ink);
    opacity: 0.8;
    margin: 7px 0 4px;
  }
  .brand-tagline {
    font-size: 14px;
    letter-spacing: 7.6px;
    line-height: 1;
    color: var(--tagline);
    margin-right: -7.6px;
  }
  .card-back {
    position: absolute;
    left: 629px;
    top: 291px;
    width: 523px;
    height: 306px;
    background: var(--back-edge);
    border: 1px solid var(--back-border);
  }
  .card-back-face {
    position: absolute;
    left: 11px;
    top: 10px;
    width: 497px;
    height: 283px;
    background: var(--card-white);
    color: var(--back-ink);
    text-align: center;
  }
  .website {
    position: absolute;
    left: 0; right: 0;
    top: 134px;
    font-size: 17px;
    letter-spacing: 3px;
  }
  .address {
    position: absolute;
    left: 0; right: 0;
    top: 203px;
    font-size: 12px;
    line-height: 19px;
    letter-spacing: 3px;
    font-style: normal;
  }
  .phone {
    position: absolute;
    left: 0; right: 0;
    top: 261px;
    font-size: 12px;
    letter-spacing: 3px;
  }
</style>
</head>
<body>
<main class="canvas">
  <section class="card-front" aria-label="Card front">
    <div class="brand">
      <div class="brand-mark"></div>
      <div class="brand-name">Casa Verbena</div>
      <div class="brand-rule"></div>
      <div class="brand-tagline">Bed &amp; Breakfast</div>
    </div>
  </section>

  <section class="card-back" aria-label="Card back">
    <div class="card-back-face">
      <p class="website">www.CasaVerbenaRetreat.example</p>
      <address class="address">LLC 3187 Partridge Fen Road<br>Larkmoor,GA 30291</address>
      <p class="phone">Tel. 770-555-0193</p>
    </div>
  </section>
</main>
</body>
</html>
```